Business Card Design

We do Metal Roofing, fascia and gutter and edge protection [safety rail].

Industry/Entity Type

Business

Contact Information for Business Card

Tallowind Roof Plumbing. Metal Roofing, Fascia and Gutter, Edge Protection
Corey 0458316072
Liam 0419563284
kv7lem4@tullanet.com
Lic: 618390K
ABN:57214603915

```html
<!DOCTYPE html>
<html lang="en">
<head>
<meta charset="utf-8">
<title>Tallowind Roof Plumbing – Business Card</title>
<link rel="stylesheet" href="https://fonts.googleapis.com/css2?family=Didact+Gothic&family=Open+Sans:wght@400;700&display=swap">
<style>
  :root {
    --brand-red: #ec1c24;
    --brand-red-deep: #c9141b;
    --charcoal: #3b3b3d;
    --charcoal-soft: #6a6a6c;
    --paper: #ffffff;
    --backdrop: #e6e6e6;
  }
  * { box-sizing: border-box; margin: 0; padding: 0; }
  html, body {
    width: 1200px; height: 900px; overflow: hidden;
    background: var(--backdrop);
  }
  .sheet {
    width: 1200px; height: 900px;
    display: flex; flex-direction: column;
    align-items: center; justify-content: center; gap: 40px;
  }
  .card {
    position: relative;
    width: 700px; height: 400px;
    overflow: hidden;
    box-shadow: 0 2px 8px rgba(0,0,0,0.12);
  }

  /* Front */
  .card--front { background: var(--brand-red); }
  .front-wordmark {
    position: absolute; left: 0; right: 0; top: 118px;
    text-align: center;
    font-family: "Didact Gothic", sans-serif;
    font-size: 112px; line-height: 1;
    color: var(--brand-red-deep);
    letter-spacing: 2px;
  }
  .front-services {
    position: absolute; left: 0; right: 0; top: 268px;
    text-align: center;
    font-family: "Open Sans", sans-serif;
    font-size: 15px; color: var(--paper);
    letter-spacing: 0.3px;
  }

  /* Back */
  .card--back { background: var(--brand-red); }
  .back-shape { position: absolute; inset: 0; }
  .back-logo {
    position: absolute; left: 46px; top: 120px;
    font-family: "Didact Gothic", sans-serif;
    color: var(--brand-red);
    font-size: 54px; line-height: 1.05;
  }
  .back-logo .logo-line { display: block; }
  .back-logo .logo-line--small { font-size: 34px; }
  .contact {
    position: absolute; right: 34px; top: 150px;
    text-align: right;
    font-family: "Open Sans", sans-serif;
    color: var(--paper);
    font-size: 16px; line-height: 1.3;
  }
  .contact .person { font-weight: 700; font-size: 18px; }
  .contact .gap { margin-top: 16px; }
  .contact .email { display: inline-flex; align-items: center; gap: 6px; }
</style>
</head>
<body>
<main class="sheet">

  <section class="card card--front" aria-label="Card front">
    <div class="front-wordmark">Tallowind</div>
    <p class="front-services">Metal Roofing, Fascia and Gutter, Edge Protection</p>
  </section>

  <section class="card card--back" aria-label="Card back">
    <svg class="back-shape" width="700" height="400" viewBox="0 0 700 400" aria-hidden="true">
      <path d="M0 0 H352 C440 110 430 290 250 400 H0 Z" fill="var(--paper)"/>
      <path d="M360 0 C452 112 442 292 262 400" fill="none" stroke="var(--charcoal)" stroke-width="9"/>
      <path d="M342 0 C428 110 418 290 240 400" fill="none" stroke="var(--charcoal-soft)" stroke-width="3"/>
    </svg>

    <div class="back-logo">
      <span class="logo-line">Tallowind</span>
      <span class="logo-line logo-line--small">Roof Plumbing</span>
    </div>

    <address class="contact" style="font-style: normal;">
      <div class="person">Corey</div>
      <div>0458316072</div>
      <div class="gap">0419563284</div>
      <div class="email">kv7lem4@tullanet.com
        <svg width="14" height="10" viewBox="0 0 14 10" aria-hidden="true">
          <rect x="0.5" y="0.5" width="13" height="9" fill="var(--paper)"/>
          <path d="M0.5 0.5 L7 6 L13.5 0.5" fill="none" stroke="var(--brand-red)" stroke-width="1.2"/>
        </svg>
      </div>
      <div class="gap">Lic: 618390K</div>
      <div>ABN:57214603915</div>
    </address>
  </section>

</main>
</body>
</html>
```